Hotdogs & Burgers restaurant needs a new menu design

We need a new menu design for our restaurant "Wurmelo". Wurmelo is a fast food specialized in hotdogs and burgers.We are looking for a simple easy menu design that walk through our customer to order the sandwich ==> the fries =>> the sides and the drinks. Wurmelo Menu:* Sandwiches**Hotdogs Our special fresh grilled hotdog served on fresh buns (Regular – 1.300 OMR / Franks – 2.000 OMR)*** DoganzaLettuce, tomato, jalapeno, pickle, onion, corn, chips, cheese, ketchup, mayo, mustard*** PepperBell pepper, onion, sweet chili sauce, avocado*** Chili FlamesChili carne, cheddar cheese, honey mustard*** ChicagoTomato, pickle, red onion, sweet relish, mustard*** New YorkGrilled onion, beef bacon, barbecue sauce, chili mustard*** Egg & CheeseOmelet, cheese, ketchup, mayo, mustard** Burgers 100% all natural beef & freshly ground, 100 grams each patty served on fresh buns.(Single patty - 2.000 OMR / double patty - 2.500 OMR)*** Sweet Beef BurgerBeef bacon, cheese, lettuce, tomato, pickle.*** Cheese Beef BurgerCheese, pickle, Wurmelo sauce.*** Mexican Beef BurgerGuacamole sauce, red onion, lettuce, tomato, Wurmelo sauce.*** Chicken BurgerFried chicken patty, lettuce, tomato, ranch sauce, Wurmelo sauce== ToppingsExtra veggies 0.100 OMRExtra cheese 0.200 OMRExtra beef Bacon 0.400 OMRExtra patty 0.500 OMR*Fries**Regular 0.600 OMR**Crispy 0.800 OMR**Wedges 0.800 OMR**Chili fries 1.500 OMRTopped with our chili carne, cheddar cheese, jalapeno, honey mustard**Lava fries 1.500 OMRTopped with fried bacon, fried onion, cheddar cheese, ranch sauce*Sides**Crispy strips 1.800 OMR5 pieces of chicken strips topped with BBQ sauce or honey mustard sauce, Wurmelo side sauce**Jalapeno cheese balls 1.300 OMR6 pieces of jalapeno cheese balls, sweet chili side sauce**Nachos 1.500 OMRA plate of nachos topped with cheddar cheese and jalapeno*Drinks**Flavored sparkling cans 0.800 OMR **Fresh orange juice 1.400 OMR**Mineral water 0.300 OMR**Soft drink 0.400 OMR**Mojito 1.500 OMRThe menu should not have any of our products pictures (icons/symbols proffered). we would prefer if the designs have unique icons/symbols created for Wurmelo. you can check our Instagram page https://www.snapfolio.example/wurmelo.official/

Industry/Entity Type

American Restaurant

Colors

Designer to choose colors to be used in the design.

Requirements
Must have
• Wurmelo Logo, Icons

```html
<!DOCTYPE html>
<html lang="en">
<head>
<meta charset="utf-8">
<title>Wurmelo Menu</title>
<link href="https://fonts.googleapis.com/css2?family=Roboto+Slab:wght@500;600;700;800&family=Fira+Sans+Condensed:wght@300;400&display=swap" rel="stylesheet">
<style>
  :root {
    --paper: #f2e9de;
    --paper-shade: #e8dccd;
    --frame: #b8825c;
    --item: #8c4a26;
    --desc: #7d5236;
    --heading: #141010;
    --accent: #8e1b12;
    --leader: #8c4a26;
  }
  html, body { margin: 0; padding: 0; overflow: hidden; background: var(--paper); }
  .menu {
    position: relative; width: 857px; height: 1200px; overflow: hidden;
    background: radial-gradient(ellipse at 30% 20%, #f5ede3 0%, var(--paper) 50%, var(--paper-shade) 100%);
    font-family: "Fira Sans Condensed", sans-serif; color: var(--desc);
  }
  .frame { position: absolute; inset: 13px; border: 1.5px solid var(--frame); }
  .abs { position: absolute; }

  .brand { left: 0; width: 857px; top: 34px; text-align: center;
    font-family: "Roboto Slab", serif; font-weight: 700; font-size: 44px; color: var(--accent); line-height: 52px; }
  .brand-dot { display: inline-block; width: 14px; height: 14px; border-radius: 50%; background: var(--accent); margin-right: 10px; vertical-align: middle; }

  .menu-title { left: 0; width: 857px; top: 110px; display: flex; justify-content: center; align-items: center; gap: 14px; }
  .menu-title span.word { font-family: "Roboto Slab", serif; font-weight: 800; font-size: 30px; color: var(--accent); letter-spacing: 1px; line-height: 34px; }
  .rule { display: block; width: 46px; height: 0; border-top: 2px solid var(--accent); }

  .section-kicker { font-family: "Roboto Slab", serif; font-weight: 600; font-size: 16px; color: var(--accent); line-height: 20px; text-align: center; }
  .section-title { font-family: "Roboto Slab", serif; font-weight: 600; font-size: 27px; color: var(--heading); line-height: 32px; text-align: center; }
  .section-note { font-size: 11.5px; line-height: 15px; text-align: center; font-weight: 300; color: var(--desc); }

  .col-left { left: 60px; width: 333px; }
  .col-right { left: 455px; width: 341px; }

  .row { display: flex; align-items: baseline; height: 20px; }
  .item-name { font-family: "Roboto Slab", serif; font-weight: 500; font-size: 16.5px; color: var(--item); line-height: 20px; white-space: nowrap; }
  .leader { flex: 1; border-bottom: 1.5px dotted var(--leader); margin: 0 1px; transform: translateY(-3px); }
  .price { font-size: 15px; color: var(--item); white-space: nowrap; }
  .item-desc { font-size: 11.5px; line-height: 15px; color: var(--desc); margin: 0; font-weight: 400; }

  .topping { position: absolute; top: 1027px; width: 96px; text-align: center; }
  .topping-photo { width: 80px; height: 80px; margin: 0 auto; border-radius: 6px; box-shadow: 0 2px 5px rgba(0,0,0,.25); }
  .topping-label { font-size: 13px; color: var(--item); line-height: 17px; margin-top: 7px; }

  .brand-foot { left: 548px; width: 250px; top: 1075px; text-align: center;
    font-family: "Roboto Slab", serif; font-weight: 700; font-size: 46px; color: var(--accent); line-height: 54px; }
</style>
</head>
<body>
<main class="menu">
  <div class="frame"></div>

  <header>
    <div class="abs brand"><span class="brand-dot"></span>Wurmelo</div>
    <div class="abs menu-title">
      <span class="rule"></span>
      <span class="word">MENU</span>
      <span class="rule"></span>
    </div>
  </header>

  <section class="abs col-left" style="top:153px">
    <div class="section-kicker">SANDWICHES</div>
    <div class="section-title">Hot Dogs</div>
    <p class="section-note" style="margin:3px 0 0">Our special fresh grilled hotdog served on fresh buns<br>(Regular – 1.300 OMR / Franks – 2.000 OMR)</p>
  </section>

  <div class="abs col-left" style="top:255px"><div class="row"><span class="item-name">Wurmelo</span><span class="leader"></span></div>
    <p class="item-desc" style="margin-top:2px">Lettuce, tomato, jalapeno, pickle, onion, corn, chips,<br>cheese, ketchup, mayo, mustard</p></div>
  <div class="abs col-left" style="top:317px"><div class="row"><span class="item-name">Pepper</span><span class="leader"></span></div>
    <p class="item-desc" style="margin-top:2px">Bell pepper, onion, sweet chili sauce, avocado</p></div>
  <div class="abs col-left" style="top:370px"><div class="row"><span class="item-name">Chili Flames</span><span class="leader"></span></div>
    <p class="item-desc" style="margin-top:6px">Chili carne, cheddar cheese, honey mustard</p></div>
  <div class="abs col-left" style="top:438px"><div class="row"><span class="item-name">Chicago</span><span class="leader"></span></div>
    <p class="item-desc" style="margin-top:5px">Tomato, pickle, red onion, sweet relish, mustard</p></div>
  <div class="abs col-left" style="top:480px"><div class="row"><span class="item-name">New York</span><span class="leader"></span></div>
    <p class="item-desc" style="margin-top:5px">Grilled onion, beef bacon, barbecue sauce, chili mustard</p></div>
  <div class="abs col-left" style="top:535px"><div class="row"><span class="item-name">Egg &amp; Cheese</span><span class="leader"></span></div>
    <p class="item-desc" style="margin-top:4px">Omelet, cheese, ketchup, mayo, mustard</p></div>

  <section class="abs col-left" style="top:598px">
    <div class="section-title">Burgers</div>
    <p class="section-note" style="margin:2px 0 0">100% all natural beef &amp; freshly ground,<br>100 grams each patty served on fresh buns.<br>(Single patty - 2.000 OMR / double patty - 2.500 OMR)</p>
  </section>

  <div class="abs col-left" style="top:699px"><div class="row"><span class="item-name">Sweet Beef Burger</span><span class="leader"></span></div>
    <p class="item-desc" style="margin-top:3px">Beef bacon, cheese, lettuce, tomato, pickle.</p></div>
  <div class="abs col-left" style="top:756px"><div class="row"><span class="item-name">Cheese Beef Burger</span><span class="leader"></span></div>
    <p class="item-desc" style="margin-top:4px">Cheese, pickle, Wurmelo sauce.</p></div>
  <div class="abs col-left" style="top:812px"><div class="row"><span class="item-name">Mexican Beef Burger</span><span class="leader"></span></div>
    <p class="item-desc" style="margin-top:5px">Fried chicken patty, lettuce, tomato, ranch sauce, Wurmelo sauce</p></div>
  <div class="abs col-left" style="top:869px"><div class="row"><span class="item-name">Chicken Burger</span><span class="leader"></span></div>
    <p class="item-desc" style="margin-top:5px">Tomato, pickle, red onion, sweet relish, mustard</p></div>

  <div class="abs section-title" style="left:110px; width:240px; top:975px">Toppings</div>
  <div class="topping" style="left:52px"><div class="topping-photo" role="img" aria-label="Photo of extra veggies" style="background:linear-gradient(135deg,#f4d28a,#e2553a 55%,#6da54a)"></div><div class="topping-label">Extra veggies<br>0.100 OMR</div></div>
  <div class="topping" style="left:165px"><div class="topping-photo" role="img" aria-label="Photo of cheese slices" style="background:linear-gradient(135deg,#fbfaf4,#f3df86 60%,#e9c95a)"></div><div class="topping-label">Extra cheese<br>0.200 OMR</div></div>
  <div class="topping" style="left:278px"><div class="topping-photo" role="img" aria-label="Photo of a burger with extra patty" style="background:linear-gradient(180deg,#7a3a1c,#c06a2c 40%,#4d2a18 70%,#d39a4a)"></div><div class="topping-label">Extra patty<br>0.500 OMR</div></div>
  <div class="topping" style="left:391px"><div class="topping-photo" role="img" aria-label="Photo of a sandwich with beef bacon" style="background:linear-gradient(180deg,#3a2a20,#c8873e 40%,#5a3722 70%,#2a1e18)"></div><div class="topping-label">Extra beef Bacon<br>0.400 OMR</div></div>

  <div class="abs col-right section-title" style="top:169px">Fries</div>
  <div class="abs col-right row" style="top:215px"><span class="item-name">Regular</span><span class="leader"></span><span class="price">0.600 OMR</span></div>
  <div class="abs col-right row" style="top:254px"><span class="item-name">Crispy</span><span class="leader"></span><span class="price">0.800 OMR</span></div>
  <div class="abs col-right row" style="top:292px"><span class="item-name">Wedges</span><span class="leader"></span><span class="price">0.800 OMR</span></div>
  <div class="abs col-right" style="top:330px"><div class="row"><span class="item-name">Chili fries</span><span class="leader"></span><span class="price">1.500 OMR</span></div>
    <p class="item-desc" style="margin-top:6px">Topped with our chili carne, cheddar cheese,<br>jalapeno, honey mustard</p></div>
  <div class="abs col-right" style="top:398px"><div class="row"><span class="item-name">Lava fries</span><span class="leader"></span><span class="price">1.500 OMR</span></div>
    <p class="item-desc" style="margin-top:6px">Topped with fried bacon, fried onion,<br>cheddar cheese, ranch sauce</p></div>

  <div class="abs col-right section-title" style="top:479px">Sides</div>
  <div class="abs col-right" style="top:523px"><div class="row"><span class="item-name">Crispy strips</span><span class="leader"></span><span class="price">1.800 OMR</span></div>
    <p class="item-desc" style="margin-top:6px">5 pieces of chicken strips topped with BBQ sauce<br>or honey mustard sauce, Wurmelo side sauce</p></div>
  <div class="abs col-right" style="top:595px"><div class="row"><span class="item-name">Jalapeno cheese balls</span><span class="leader"></span><span class="price">1.300 OMR</span></div>
    <p class="item-desc" style="margin-top:5px">6 pieces of jalapeno cheese balls,<br>sweet chili side sauce</p></div>
  <div class="abs col-right" style="top:667px"><div class="row"><span class="item-name">Nachos</span><span class="leader"></span><span class="price">1.500 OMR</span></div>
    <p class="item-desc" style="margin-top:6px">A plate of nachos topped with<br>cheddar cheese and jalapeno</p></div>

  <div class="abs col-right section-title" style="top:743px">Drinks</div>
  <div class="abs col-right row" style="top:787px"><span class="item-name">Flavored sparkling cans</span><span class="leader"></span><span class="price">0.800 OMR</span></div>
  <div class="abs col-right row" style="top:826px"><span class="item-name">Fresh orange juice</span><span class="leader"></span><span class="price">1.400 OMR</span></div>
  <div class="abs col-right row" style="top:866px"><span class="item-name">Mineral water</span><span class="leader"></span><span class="price">0.300 OMR</span></div>
  <div class="abs col-right row" style="top:905px"><span class="item-name">Soft drink</span><span class="leader"></span><span class="price">0.400 OMR</span></div>
  <div class="abs col-right row" style="top:946px"><span class="item-name">Mojito</span><span class="leader"></span><span class="price">1.500 OMR</span></div>

  <footer class="abs brand-foot">Wurmelo</footer>
</main>
</body>
</html>
```